Cleaning Company needs a new business card design

Hi, We are looking for new business card designs to update with our latest logo and company information.
We would like to see designs using the colours:
Royal Blue #4169E1 - this is our company colour so this has to be in there. Please feel free to experiment with other colours.
Must include:
Front of business card:
Logo
Back of the business card:
0800 529 6081
07438 915 702
Email: info@pkrtidyhomes.co.uk
Web: www.pkrtidyhomes.co.uk
Services:
End of Tenancy
Carpet & Upholstery
Regular & One Off
all work fully insured.
The front of the business card with the logo can be made to look raised print. The blue man to be a shiny finish.
The business card needs to be presented in a matt finish
The business must be in the following styles:
Standard Square with rounded corners.
Thank you to all that take part in this.
Target Market(s)
Men and Women of different ages in the UK.
Industry/Entity Type
House Cleaning
Contact Information for Business Card
Front of business card:
Logo
0800 529 6081
07438 915 702
Email: pkrtidy@mailbox-demo.co.uk
Services:
End of Tenancy
Carpet & Upholstery
Regular & One Off
all work fully insured.

```html
<!DOCTYPE html>
<html lang="en">
<head>
<meta charset="utf-8">
<title>PKR Tidy Homes – Business Card</title>
<link href="https://fonts.googleapis.com/css2?family=Didact+Gothic&display=swap" rel="stylesheet">
<style>
  :root{
    --page:#e9ebef;
    --royal:#4169e1;
    --navy:#1f3f9e;
    --deep:#17338a;
    --sky:#3fb3e0;
    --paper:#f3f1ee;
    --white:#ffffff;
    --drop:#6fa6e6;
  }
  *{box-sizing:border-box;margin:0;padding:0}
  html,body{width:1200px;height:800px;overflow:hidden;background:var(--page)}
  body{font-family:"Didact Gothic",sans-serif;position:relative}
  .card{position:absolute;width:525px;height:300px;border-radius:18px;overflow:hidden;box-shadow:0 8px 24px rgba(20,30,60,.18)}
  .card-front{left:50px;top:250px;background:var(--paper);display:flex;align-items:center;justify-content:center}
  .brand{display:flex;align-items:center;gap:14px}
  .brand-dot{width:26px;height:26px;border-radius:50%;background:var(--sky);flex:none}
  .brand-name{font-size:36px;color:var(--navy);letter-spacing:.5px;line-height:1}
  .brand-sub{display:block;font-size:17px;color:var(--navy);margin-top:6px}
  .card-back{left:625px;top:250px;background:linear-gradient(160deg,#3d6fd8 0%,var(--royal) 35%,var(--deep) 100%);color:var(--white)}
  .back-art{position:absolute;inset:0;width:100%;height:100%}
  .back-brand{position:absolute;left:24px;top:58px;display:flex;align-items:center;gap:10px}
  .back-brand .brand-dot{width:18px;height:18px;background:var(--white)}
  .back-brand .brand-name{color:var(--white);font-size:25px}
  .back-brand .brand-sub{color:var(--white);font-size:13px}
  .divider{position:absolute;left:258px;top:24px;width:1.5px;height:168px;background:rgba(255,255,255,.8)}
  .contact{position:absolute;left:276px;top:24px;list-style:none;font-size:13.5px;line-height:23px}
  .contact li{display:flex;align-items:center;gap:8px}
  .icon{width:12px;height:12px;flex:none;fill:var(--white)}
  .services{position:absolute;left:276px;top:120px}
  .services h2{font-weight:400;font-size:19px;margin-bottom:2px}
  .services ul{list-style:none;font-size:14px;line-height:23px}
  .services li{display:flex;align-items:center;gap:8px}
  .bullet{width:11px;height:11px;border-radius:50%;background:var(--white);flex:none}
</style>
</head>
<body>
  <section class="card card-front" aria-label="Business card front">
    <div class="brand">
      <span class="brand-dot"></span>
      <span class="brand-name">PKR Tidy Homes<span class="brand-sub">Limited</span></span>
    </div>
  </section>

  <section class="card card-back" aria-label="Business card back">
    <svg class="back-art" viewBox="0 0 525 300" preserveAspectRatio="none">
      <rect width="525" height="300" fill="transparent" role="img" aria-label="Photograph of water droplets on blue glass"/>
      <path d="M0 135 C60 232 200 264 330 264 C430 264 490 244 525 220 L525 300 L0 300 Z" fill="#6fa6e6" opacity=".55" role="img" aria-label="Band of water droplets"/>
      <path d="M0 135 C60 232 200 264 330 264 C430 264 490 244 525 220" fill="none" stroke="#bfe6ff" stroke-width="3"/>
      <path d="M0 147 C62 242 200 274 330 274 C432 274 492 254 525 232" fill="none" stroke="#3fb3e0" stroke-width="2"/>
    </svg>

    <div class="back-brand">
      <span class="brand-dot"></span>
      <span class="brand-name">PKR Tidy Homes<span class="brand-sub">Limited</span></span>
    </div>

    <div class="divider"></div>

    <ul class="contact">
      <li><svg class="icon" viewBox="0 0 12 12"><rect x="3" y="0.5" width="6" height="11" rx="1.2"/></svg>0800 529 6081</li>
      <li><svg class="icon" viewBox="0 0 12 12"><path d="M2 1l2.5 0 1 3-1.5 1a7 7 0 0 0 3 3l1-1.5 3 1V10a1.5 1.5 0 0 1-1.5 1.5A9.5 9.5 0 0 1 .5 2.5 1.5 1.5 0 0 1 2 1z"/></svg>07438 915 702</li>
      <li><svg class="icon" viewBox="0 0 12 12"><circle cx="6" cy="6" r="5.5"/></svg>info@pkrtidyhomes.co.uk</li>
      <li><svg class="icon" viewBox="0 0 12 12"><rect x="1" y="2" width="10" height="8" rx="1"/></svg>www.pkrtidyhomes.co.uk</li>
    </ul>

    <div class="services">
      <h2>Services</h2>
      <ul>
        <li><span class="bullet"></span>End of Tenancy</li>
        <li><span class="bullet"></span>Carpet &amp; Upholstery</li>
        <li><span class="bullet"></span>Regular &amp; One Off</li>
      </ul>
    </div>
  </section>
</body>
</html>
```